Bookcover: Lessons From the Silent Orchard

I am publishing a super-low-cost innovation book for €4,99 on Bravolo Self Release to help everyone become a great innovator: young ambitious people without college education nor a big budget. Do you want to help me?

Brief:
Design a book cover 1600 x 2560 pixels for BSR.
Main title: Lessons From the Silent Orchard
Sub title: mindset - insights - skills & tools
Author: Maarten de Klerk
Design: captive, and appealing to everyone
Target Group: young ambitious people without college education

For bravolo please format the height/width ratio of 1.6:1

```html
<!DOCTYPE html>
<html lang="en">
<head>
<meta charset="utf-8">
<title>Lessons From the Silent Orchard – Book Cover</title>
<link rel="stylesheet" href="https://fonts.googleapis.com/css2?family=Bebas+Neue&family=Montserrat:wght@400;500&display=swap">
<style>
  :root {
    --page: #ffffff;
    --cover: #171f27;
    --cover-deep: #11181f;
    --board-glow: #6b747c;
    --board-light: #4b545c;
    --board-mid: #333c45;
    --board-dark: #222a32;
    --accent: #c8174a;
    --paper: #ec4a63;
    --paper-light: #f47a8a;
    --paper-dark: #c92f4b;
    --ink: #ffffff;
  }
  html, body {
    margin: 0;
    padding: 0;
    width: 1200px;
    height: 1200px;
    overflow: hidden;
    background: var(--page);
  }
  .cover {
    position: absolute;
    left: 240px;
    top: 24px;
    width: 720px;
    height: 1152px;
    background: var(--cover);
    overflow: hidden;
  }
  .cover__artwork {
    position: absolute;
    left: 0;
    top: 520px;
    width: 720px;
    height: 632px;
    background:
      radial-gradient(ellipse 108px 90px at 368px 252px, var(--paper-light) 0%, var(--paper) 45%, var(--paper-dark) 88%, transparent 100%),
      radial-gradient(ellipse 190px 160px at 368px 252px, rgba(236, 74, 99, 0.18) 0%, transparent 100%),
      radial-gradient(ellipse 260px 230px at 368px 260px, var(--board-glow) 0%, var(--board-light) 35%, transparent 100%),
      radial-gradient(ellipse 420px 360px at 380px 290px, var(--board-mid) 0%, var(--board-dark) 70%, transparent 100%),
      linear-gradient(to bottom, var(--cover) 0%, var(--board-dark) 14%, var(--board-mid) 45%, var(--board-dark) 78%, var(--cover-deep) 100%);
  }
  .cover__series {
    position: absolute;
    left: 0;
    right: 0;
    top: 46px;
    margin: 0;
    text-align: center;
    font-family: "Montserrat", sans-serif;
    font-weight: 400;
    font-size: 27px;
    letter-spacing: 1px;
    color: var(--ink);
    text-transform: uppercase;
  }
  .cover__rule {
    position: absolute;
    left: 76px;
    width: 568px;
    top: 90px;
    height: 2px;
    background: var(--accent);
  }
  .cover__title {
    position: absolute;
    left: 0;
    right: 0;
    top: 136px;
    margin: 0;
    text-align: center;
    font-family: "Bebas Neue", "Oswald", sans-serif;
    font-weight: 400;
    line-height: 1;
  }
  .cover__title-lead {
    display: block;
    font-size: 92px;
    color: var(--accent);
    letter-spacing: 1px;
  }
  .cover__title-main {
    display: block;
    font-size: 188px;
    line-height: 0.83;
    color: var(--ink);
  }
  .cover__author {
    position: absolute;
    left: 0;
    right: 0;
    top: 1050px;
    margin: 0;
    text-align: center;
    font-family: "Montserrat", sans-serif;
    font-weight: 500;
    font-size: 52px;
    letter-spacing: 0;
    color: var(--ink);
    text-transform: uppercase;
  }
</style>
</head>
<body>
  <main class="cover">
    <div class="cover__artwork" role="img" aria-label="Dark chalkboard filled with hand-drawn business sketches, charts and formulas, with a crumpled pink paper ball glowing at its centre"></div>
    <p class="cover__series">Mindset - Insights - Skills &amp; Tools</p>
    <div class="cover__rule"></div>
    <h1 class="cover__title">
      <span class="cover__title-lead">Lessons From the</span>
      <span class="cover__title-main">Silent</span>
      <span class="cover__title-main">Orchard</span>
    </h1>
    <p class="cover__author">Maarten de Klerk</p>
  </main>
</body>
</html>
```